I need a business card for myself, being a proprietor of a funeral parlor based in Manila. I'd like the card to have either of the following:
White Font on Black Background
or
Black Font on White Background
No logo is needed however I will appreciate any efforts to show a symbol of eternal happiness, aptly designed with above mentioned colors in mind.
Company name, address and contact on the lower right corner.
Logo or symbol anywhere.
Quillstone Funeral Services
+639174826351
darvik4521@pelmora.com
corner of Brisco Avenue and Velhurst Street
Makati City, Philippines
Thank you.
Update: Please include a small dove in your design. You are free to choose where you would like it on the card.

```html
<!DOCTYPE html>
<html lang="en">
<head>
<meta charset="utf-8">
<title>Quillstone Funeral Services – Business Card</title>
<link rel="stylesheet" href="https://fonts.googleapis.com/css2?family=Roboto+Condensed:wght@400;700&display=swap">
<style>
  :root {
    --sheet: #ffffff;
    --card: #202020;
    --card-shade: #383838;
    --panel: #ffffff;
    --symbol: #222222;
    --ink: #ffffff;
    --trim: #e0262b;
    --mark: #333333;
  }
  * { box-sizing: border-box; margin: 0; padding: 0; }
  html, body { width: 1200px; height: 872px; overflow: hidden; background: var(--sheet); }
  .sheet { position: relative; width: 1200px; height: 872px; }

  .crop-mark { position: absolute; background: var(--mark); }
  .crop-mark.v { width: 1px; height: 17px; }
  .crop-mark.h { width: 17px; height: 1px; }

  .card {
    position: absolute; left: 341px; top: 273px; width: 517px; height: 326px;
    background: var(--card); outline: 1px solid var(--trim); overflow: hidden;
    font-family: "Roboto Condensed", "Arial Narrow", sans-serif; color: var(--ink);
  }
  .card__shade {
    position: absolute; left: 200px; top: 0; width: 317px; height: 326px;
    background: radial-gradient(ellipse at 70% 45%, var(--card-shade) 0%, var(--card-shade) 35%, var(--card) 75%);
  }
  .card__panel {
    position: absolute; left: 33px; top: 0; width: 118px; height: 241px; background: var(--panel);
  }
  .card__symbol {
    position: absolute; left: 6px; top: 56px; width: 106px; height: 165px; background: var(--symbol);
  }
  .card__info {
    position: absolute; left: 167px; width: 320px; top: 100px; text-align: center;
  }
  .company-name { font-weight: 700; font-size: 26px; line-height: 32px; letter-spacing: 0.2px; }
  .address { margin-top: 12px; font-size: 15px; line-height: 20px; }
  .contact { font-size: 15px; line-height: 27px; }
  .phone { margin-top: 17px; }
  .icon { display: inline-block; width: 13px; height: 13px; vertical-align: -2px; margin-right: 2px; }
</style>
</head>
<body>
<div class="sheet">
  <span class="crop-mark v" style="left:357px;top:257px"></span>
  <span class="crop-mark v" style="left:841px;top:257px"></span>
  <span class="crop-mark v" style="left:357px;top:599px"></span>
  <span class="crop-mark v" style="left:841px;top:599px"></span>
  <span class="crop-mark h" style="left:324px;top:290px"></span>
  <span class="crop-mark h" style="left:858px;top:290px"></span>
  <span class="crop-mark h" style="left:324px;top:582px"></span>
  <span class="crop-mark h" style="left:858px;top:582px"></span>

  <div class="card">
    <div class="card__shade" role="img" aria-label="Large faint flowing ornamental shapes in dark grey"></div>
    <div class="card__panel">
      <div class="card__symbol" role="img" aria-label="Ornate black gothic cross"></div>
    </div>

    <div class="card__info">
      <h1 class="company-name">Quillstone Funeral Services</h1>
      <p class="address">
        <svg class="icon" viewBox="0 0 14 14" aria-hidden="true"><path d="M7 1a4.5 4.5 0 0 1 4.5 4.5C11.5 9 7 13 7 13S2.5 9 2.5 5.5A4.5 4.5 0 0 1 7 1z" fill="none" stroke="#fff" stroke-width="1"/><circle cx="7" cy="5.6" r="1.5" fill="#fff"/></svg>: Corner of Brisco Avenue and Velhurst Street,<br>Makati City, Philippines
      </p>
      <p class="contact phone">
        <svg class="icon" viewBox="0 0 14 14" aria-hidden="true"><circle cx="7" cy="7" r="6.2" fill="none" stroke="#fff" stroke-width="1"/><path d="M4.6 3.8l1.3-.3.8 1.8-.9.7c.4.9 1.1 1.6 2 2l.7-.9 1.8.8-.3 1.3c-3 .2-5.6-2.4-5.4-5.4z" fill="#fff"/></svg>: +639174826351
      </p>
      <p class="contact email">
        <svg class="icon" viewBox="0 0 14 14" aria-hidden="true"><circle cx="7" cy="7" r="6.2" fill="none" stroke="#fff" stroke-width="1"/><rect x="3.5" y="4.5" width="7" height="5" fill="none" stroke="#fff" stroke-width="0.9"/><path d="M3.5 4.5L7 7.5l3.5-3" fill="none" stroke="#fff" stroke-width="0.9"/></svg>: darvik4521@pelmora.com
      </p>
    </div>
  </div>
</div>
</body>
</html>
```